Business IT Services Billboard to attract local small businesses

We are Brivolane, a premier Managed Service Provider (MSP) specializing in comprehensive IT services and VOIP phone solutions exclusively for businesses. Our goal is to create a dynamic and visually engaging billboard advertisement that not only highlights our cutting-edge IT solutions but also emphasizes our state-of-the-art VOIP phone services. This billboard should communicate our commitment to providing innovative, reliable, and holistic technology solutions.
Target Market(s)
small business
Industry/Entity Type
Information Technology
Colors
Designer to choose colors to be used in the design.
Look and feel
Each slider illustrates characteristics of the customer's brand and the style your logo design should communicate.

```html
<!DOCTYPE html>
<html lang="en">
<head>
<meta charset="UTF-8">
<title>Brivolane Billboard</title>
<link href="https://fonts.googleapis.com/css2?family=Montserrat:wght@500;600;700;800;900&display=swap" rel="stylesheet">
<style>
  :root {
    --brand-blue: #0b68b5;
    --band-blue: #0a5a9c;
    --band-deep: #064680;
    --navy: #123f73;
    --accent-blue: #1279c9;
    --ink: #1f3550;
    --white: #ffffff;
    --page: #eef1f5;
    --photo-light: #8f9bab;
    --photo-dark: #3c4654;
  }
  * { margin: 0; padding: 0; box-sizing: border-box; }
  html, body {
    width: 1189px;
    height: 1200px;
    overflow: hidden;
    background: var(--page);
    font-family: "Montserrat", sans-serif;
  }
  .billboard {
    position: absolute;
    left: 44px;
    top: 440px;
    width: 1100px;
    height: 320px;
    background: var(--white);
    box-shadow: 0 6px 24px rgba(0, 0, 0, 0.15);
    overflow: hidden;
  }
  .billboard-shapes {
    position: absolute;
    inset: 0;
    width: 1100px;
    height: 320px;
  }
  .brand-name {
    position: absolute;
    left: 34px;
    top: 10px;
    font-weight: 900;
    font-size: 62px;
    line-height: 62px;
    letter-spacing: 9px;
    color: var(--brand-blue);
  }
  .headline {
    position: absolute;
    left: 36px;
    top: 92px;
    font-weight: 800;
    font-size: 36px;
    line-height: 39px;
    color: var(--white);
    text-transform: uppercase;
  }
  .tagline {
    position: absolute;
    left: 36px;
    top: 214px;
    padding-left: 9px;
    border-left: 2px solid var(--white);
    font-weight: 500;
    font-size: 15.5px;
    line-height: 17px;
    letter-spacing: 0.4px;
    color: var(--white);
  }
  .cta-row {
    position: absolute;
    left: 0;
    right: 0;
    top: 266px;
    height: 54px;
    display: flex;
    align-items: center;
    justify-content: center;
    gap: 14px;
    white-space: nowrap;
  }
  .cta-lead {
    font-weight: 500;
    font-size: 22px;
    letter-spacing: 0.3px;
    color: var(--ink);
  }
  .cta-url {
    font-weight: 800;
    font-size: 27px;
    color: var(--brand-blue);
  }
  .cta-divider {
    width: 2px;
    height: 28px;
    background: var(--ink);
  }
  .cta-phone {
    font-weight: 800;
    font-size: 27px;
    color: var(--navy);
  }
</style>
</head>
<body>
  <section class="billboard">
    <svg class="billboard-shapes" viewBox="0 0 1100 320" xmlns="http://www.w3.org/2000/svg">
      <defs>
        <linearGradient id="bandGradient" x1="0" y1="0" x2="1" y2="1">
          <stop offset="0" stop-color="var(--band-blue)"/>
          <stop offset="1" stop-color="var(--band-deep)"/>
        </linearGradient>
        <linearGradient id="photoGradient" x1="0" y1="0" x2="1" y2="1">
          <stop offset="0" stop-color="var(--photo-dark)"/>
          <stop offset="0.55" stop-color="var(--photo-light)"/>
          <stop offset="1" stop-color="#c9b08a"/>
        </linearGradient>
      </defs>
      <rect class="message-band" x="0" y="78" width="1100" height="188" fill="url(#bandGradient)"/>
      <polygon class="header-strip" points="0,0 672,0 640,78 0,78" fill="var(--white)"/>
      <polygon class="divider-wedge" points="665,0 714,0 610,266 560,266" fill="var(--navy)"/>
      <polygon class="team-photo" role="img" aria-label="Photo of three business colleagues working together at a laptop in a bright office"
               points="714,0 1100,0 1100,266 610,266" fill="url(#photoGradient)"/>
      <polygon class="accent-triangle" points="636,200 610,266 676,266" fill="var(--accent-blue)"/>
      <line class="divider-line" x1="700" y1="0" x2="598" y2="262" stroke="var(--white)" stroke-width="3"/>
    </svg>

    <div class="brand-name">BRIVOLANE</div>

    <h1 class="headline">Elevate your business<br>with next-gen IT and<br>VOIP services</h1>

    <p class="tagline">Innovative IT and VOIP Solutions Tailored<br>for Your Business Success.</p>

    <div class="cta-row">
      <span class="cta-lead">Transform Your Tech Today at</span>
      <span class="cta-url">www.brivolane.com</span>
      <span class="cta-divider"></span>
      <span class="cta-phone">Call (555) 014-2290</span>
    </div>
  </section>
</body>
</html>
```